Bright Harbor Charity - helping the disadvantaged

I would like a new web site design for my charity BRIGHT HARBOR. The charity provides help for the disadvantaged. See current site
brightharbor.org.au for details. Please refer to the current site for information on the charity. The objectives of the charity are in the "about us" tab. You will also notice on the site that we provide information about events that we sponsor an area for this should be provided on the site.

Target Market(s)

We have two targets:
1. Individuals and Businesses that will donate money to the charity.
2. Individuals that are in need of support from the charity.

Industry/Entity Type

Charity

Requirements
Must have
• Ability for individuals to be able to understand the type of support we can provide.
Nice to have
• Our logo should be prominate on each pages
Should not have
• Should be use modern fonts

```html
<!DOCTYPE html>
<html lang="en">
<head>
<meta charset="utf-8">
<title>Bright Harbor – Helping the Disadvantaged</title>
<link href="https://fonts.googleapis.com/css2?family=Open+Sans:wght@400;600;700;800&family=Arimo:wght@400;700&display=swap" rel="stylesheet">
<style>
:root{
  --sky-top:#4a9fd6;
  --sky-mid:#8fd0ec;
  --sky-low:#b9e6f4;
  --panel:#1b9fc4;
  --panel-dark:#1587ab;
  --panel-line:#4fb8d6;
  --nav-green:#2f7d16;
  --nav-green-light:#4d9a22;
  --orange:#f07a0c;
  --red:#d9352c;
  --white:#ffffff;
  --text-light:#e6f6fb;
  --footer:#0b7596;
  --footer-text:#e9f6fa;
  --logo-green:#4f8f1e;
  --gold:#e0a21a;
}
*{box-sizing:border-box;margin:0;padding:0}
html,body{width:933px;height:1200px;overflow:hidden}
body{font-family:"Arimo",Arial,sans-serif;background:var(--sky-low)}
.canvas{position:relative;width:933px;height:1200px;overflow:hidden;
  background:linear-gradient(180deg,var(--sky-top) 0,var(--sky-mid) 420px,var(--sky-low) 700px,#c7ecf6 980px)}
.abs{position:absolute}

.login{left:767px;top:0;width:57px;height:29px;background:var(--orange);color:var(--white);
  font:700 11px "Open Sans",sans-serif;display:flex;align-items:center;justify-content:center;border-radius:0 0 3px 3px}

.brand{left:0;width:933px;top:62px;display:flex;justify-content:center;align-items:center;gap:10px}
.brand-mark{width:16px;height:16px;border-radius:50%;background:var(--gold)}
.brand-name{font:700 38px "Open Sans",sans-serif;color:var(--logo-green);letter-spacing:1px}

.nav{left:93px;top:123px;width:758px;height:34px;background:linear-gradient(180deg,var(--nav-green-light),var(--nav-green));
  display:flex;align-items:center;justify-content:space-around;padding:0 18px;box-shadow:0 2px 3px rgba(0,0,0,.25)}
.nav a{color:var(--white);text-decoration:none;font:600 12px "Open Sans",sans-serif;text-transform:uppercase;padding:4px 6px}
.nav a.active{background:var(--orange);border-radius:3px}

.hero{left:100px;top:157px;width:735px;height:292px;background:linear-gradient(180deg,#2aa7cd,#1e9cc4 60%,#2bb0d3)}
.hero-photo{left:23px;top:28px;width:353px;height:238px;border-radius:8px;
  background:linear-gradient(135deg,#6e5a48,#b8a48c 55%,#8a7460);box-shadow:0 0 0 5px #4ac0e0}
.hero-title{left:433px;top:43px;width:290px;color:var(--white);font:700 27px/1.12 "Open Sans",sans-serif;text-transform:uppercase}
.hero-title small{font-size:15px;vertical-align:super}
.hero-text{left:433px;top:130px;width:270px;color:var(--text-light);font:11px/1.35 "Arimo",sans-serif}
.donate{left:436px;top:188px;width:184px;height:43px}
.slide-arrow{top:285px;width:34px;height:50px}

.main{left:97px;top:465px;width:740px;height:492px;background:var(--panel);border-radius:4px;box-shadow:0 2px 6px rgba(0,0,0,.25)}
.section-title{color:var(--white);font:700 14px "Open Sans",sans-serif;text-transform:uppercase}
.rule{height:1px;background:var(--panel-line)}
.event-image{left:23px;top:55px;width:263px;height:140px;background:linear-gradient(180deg,#222,#2e2e2e);border:3px solid #d8d8d8}
.event-title{left:315px;top:53px;width:330px;color:var(--white);font:700 17px/1.15 "Open Sans",sans-serif;text-transform:uppercase}
.event-meta{left:315px;top:94px;color:#bfe6f2;font:10px "Arimo",sans-serif}
.event-text{left:315px;top:113px;width:330px;color:var(--text-light);font:10.5px/1.4 "Arimo",sans-serif}
.pill{height:22px;display:flex;align-items:center}
.pill span{position:absolute;left:12px;top:4px;color:var(--white);font:700 10.5px "Arimo",sans-serif}

.child-photo{width:120px;height:120px;border-radius:50%;border:4px solid var(--white)}
.child-info{width:200px;color:var(--text-light);font:10.5px/1.38 "Arimo",sans-serif}
.child-info dl{display:grid;grid-template-columns:60px 1fr;row-gap:9px;color:var(--white);font:700 11px "Arimo",sans-serif;text-transform:uppercase;margin-bottom:12px}
.child-info b{color:var(--white)}
.divider{left:368px;top:255px;width:1px;height:215px;background:#1480a3}

.footer{left:0;top:980px;width:933px;height:220px;background:var(--footer);color:var(--footer-text)}
.footer h3{font:700 14px "Arimo",sans-serif;color:var(--white)}
.footer p{font:10.5px/1.45 "Arimo",sans-serif}
.sub-title{color:var(--white);font:700 17px "Arimo",sans-serif}
.sub-field{width:148px;height:22px;background:var(--white);border:1px solid #aaa;color:#888;font:10px "Arimo",sans-serif;padding:4px 6px}
.footer-links{left:118px;top:162px;font:10px "Arimo",sans-serif;color:var(--white)}
.copyright{left:118px;top:182px;font:9px "Arimo",sans-serif;color:var(--white)}
</style>
</head>
<body>
<div class="canvas">

  <a class="abs login">LOGIN</a>

  <div class="abs brand">
    <span class="brand-mark"></span>
    <span class="brand-name">BRIGHT HARBOR</span>
  </div>

  <nav class="abs nav">
    <a class="active">Home</a><a>Artist Gallery</a><a>Signatures</a><a>Blog</a><a>Best Sellers</a><a>Press</a><a>Contact</a>
  </nav>

  <svg class="abs slide-arrow" style="left:36px" viewBox="0 0 34 50"><polyline points="28,4 6,25 28,46" fill="none" stroke="#6aa8c4" stroke-width="5"/></svg>
  <svg class="abs slide-arrow" style="left:863px" viewBox="0 0 34 50"><polyline points="6,4 28,25 6,46" fill="none" stroke="#6aa8c4" stroke-width="5"/></svg>

  <section class="abs hero">
    <div class="abs hero-photo" role="img" aria-label="Volunteer helping children draw on paper sheets on a classroom floor"></div>
    <h1 class="abs hero-title">Direct assistance to people in need in <small>Australia</small></h1>
    <p class="abs hero-text">People in need includes orphaned children, disabled people, people living under poverty, distress, misfortune or destitution, people suffering from sickness.</p>
    <svg class="abs donate" viewBox="0 0 184 43">
      <polygon points="0,0 170,0 184,21.5 170,43 0,43" fill="#2f7d16"/>
      <polygon points="0,0 170,0 184,21.5 0,21.5" fill="#4d9a22"/>
      <text x="12" y="27" fill="#fff" font-family="Open Sans, sans-serif" font-weight="700" font-size="15">MAKE A DONATION</text>
    </svg>
  </section>

  <main class="abs main">
    <h2 class="abs section-title" style="left:21px;top:18px">News &amp; Events</h2>
    <div class="abs rule" style="left:21px;top:41px;width:697px"></div>

    <div class="abs event-image" role="img" aria-label="Harmony Day banner, 24 March, with a row of paper-chain figures"></div>
    <h3 class="abs event-title">Harmony Day information sheet &amp; booking form</h3>
    <div class="abs event-meta">August 19, 2011 - Posted in:- News</div>
    <p class="abs event-text">Riverbend's Inaugural Harmony Day Event 2012 Harmony Celebration Day – "EVERYONE BELONGS" Date: Saturday 24th March 2012 Venue: Elmwood Learning Centre, Linden Road, Marlow. Time: 10am – 3pm. Harmony Day is celebrated.</p>
    <div class="abs pill" style="left:315px;top:172px">
      <svg width="96" height="22" viewBox="0 0 96 22"><polygon points="0,0 86,0 96,11 86,22 0,22" fill="#d9352c"/></svg>
      <span>Read More</span>
    </div>

    <h2 class="abs section-title" style="left:21px;top:230px">Sponsor a Child</h2>
    <div class="abs rule" style="left:21px;top:251px;width:697px"></div>
    <div class="abs divider"></div>

    <div class="abs child-photo" style="left:23px;top:262px;background:radial-gradient(circle at 50% 40%,#f2c9a8,#d86a6a 70%,#e9e4d6)" role="img" aria-label="Smiling young girl, Lisa"></div>
    <div class="abs child-info" style="left:155px;top:262px">
      <dl><dt>Name:</dt><dd>Lisa</dd><dt>Age:</dt><dd>6 yr old</dd></dl>
      <p><b>Background:</b> Mother (house maid), Father (Vegetable seller), Sister (8yrs old).</p>
      <p style="margin-top:8px">About: Struggles with her alphabet grasping problem tries hard to memorise them, now has started recognising the alphabets steadily. Loves to dance, sing and colour, a cheerful girl loves to play.</p>
    </div>
    <div class="abs pill" style="left:157px;top:430px">
      <svg width="100" height="20" viewBox="0 0 100 20"><polygon points="0,0 90,0 100,10 90,20 0,20" fill="#d9352c"/></svg>
      <span style="top:4px;font-size:9.5px">Sponsor This Girl</span>
    </div>

    <div class="abs child-photo" style="left:400px;top:262px;background:radial-gradient(circle at 50% 45%,#6b4632,#3a6a3a 70%,#9a8a6a)" role="img" aria-label="Smiling young boy, John"></div>
    <div class="abs child-info" style="left:534px;top:262px">
      <dl><dt>Name:</dt><dd>John</dd><dt>Age:</dt><dd>8 yr old</dd></dl>
      <p><b>Background:</b> Mother (house maid), Father (Vegetable seller), Sister (8yrs old).</p>
      <p style="margin-top:8px">About: Struggles with her alphabet grasping problem tries hard to memorise them, now has started recognising the alphabets steadily. Loves to dance, sing and colour, a cheerful girl loves to play.</p>
    </div>
    <div class="abs pill" style="left:534px;top:430px">
      <svg width="100" height="20" viewBox="0 0 100 20"><polygon points="0,0 90,0 100,10 90,20 0,20" fill="#d9352c"/></svg>
      <span style="top:4px;font-size:9.5px">Sponsor This Boy</span>
    </div>
  </main>

  <footer class="abs footer">
    <h3 class="abs" style="left:118px;top:42px">Aabout Us</h3>
    <p class="abs" style="left:118px;top:64px;width:310px">Lorem Ipsum is simply dummy text of the printing and typesetting industry. Lorem Ipsum has been the industry's standard dummy text ever since the 1500s, when an unknown printer took a galley of type and scrambled it to make a type specimen book. It has survived not only five centuries, but also the leap into electronic typesetting.</p>

    <h3 class="abs" style="left:476px;top:42px">Contact Us</h3>
    <p class="abs" style="left:476px;top:64px;width:170px;font-size:9.5px">Harbour Light Community Service<br>18 Harbour Street<br>Marlow, NSW 2577<br>Phone No. : (400) 555-0147<br>Fax No. : (400) 555-0148<br><span style="color:#8fcfe4">info@brightharbor.org.au</span></p>

    <svg class="abs" style="left:638px;top:4px" width="186" height="150" viewBox="0 0 186 150">
      <path d="M40 30 C40 8 70 2 86 14 C100 0 132 4 140 20 C162 16 182 32 176 52 C190 66 180 94 160 96 C160 116 130 124 112 112 C98 126 66 126 56 110 C40 118 18 108 22 90 C4 84 2 58 18 50 C10 34 24 26 40 30 Z" fill="#0a6583"/>
      <path d="M36 112 L10 146 L52 116 Z" fill="#0a6583"/>
    </svg>
    <div class="abs sub-title" style="left:692px;top:42px">Subscribe</div>
    <div class="abs sub-field" style="left:662px;top:70px">Enter Your Email Address</div>
    <div class="abs pill" style="left:705px;top:104px">
      <svg width="74" height="22" viewBox="0 0 74 22"><polygon points="0,0 64,0 74,11 64,22 0,22" fill="#d9352c"/></svg>
      <span style="left:12px">Submit</span>
    </div>

    <div class="abs footer-links">Home | About Us | Donate | Apply | Pledge | Nominate | Events | Contact Us | Directors</div>
    <div class="abs copyright">© Copyright 2012 BRIGHT HARBOR. All Rights Reserved. Terms &amp; Conditions | Privacy Policy</div>
  </footer>

</div>
</body>
</html>
```